We are Harwell Heart and Circulatory Care and located at 2945 Pelton Avenue, Suites 300 & 400, Winchester, VA 22784. Our phone is 540-318-4971 We are creating a brochure to promote our Arrhythmia Clinic. Our audience is both patients and referring to help education and understand our arrhythmias. Please add imaging. We appreciate any create suggestions when comes to imaging as long as relates to medical information being provided.

```html
<!DOCTYPE html>
<html lang="en">
<head>
<meta charset="utf-8">
<title>Harwell Heart and Circulatory Care – Arrhythmia Clinic Brochure</title>
<link href="https://fonts.googleapis.com/css2?family=Open+Sans:wght@400;600;700;800&display=swap" rel="stylesheet">
<style>
  :root {
    --crimson: #a3152b;
    --maroon: #6b0010;
    --charcoal: #3f3f41;
    --ink: #2a2a2a;
    --paper: #ffffff;
    --stage: #e4e4e6;
    --soft-rose: #f6e3e6;
    --font: "Open Sans", Arial, sans-serif;
  }
  * { box-sizing: border-box; margin: 0; padding: 0; }
  html, body { width: 1200px; height: 900px; overflow: hidden; }
  body { background: var(--stage); font-family: var(--font); color: var(--ink); position: relative; }

  .page { position: absolute; width: 560px; height: 390px; background: var(--paper); overflow: hidden; box-shadow: 0 6px 18px rgba(0,0,0,.18); }
  .page--about { left: 40px; top: 30px; }
  .page--more { left: 600px; top: 30px; }
  .page--cover { left: 320px; top: 470px; }

  /* Footer band shared by inside pages */
  .footer-band { position: absolute; left: 0; bottom: 0; width: 100%; height: 44px; }
  .footer-url { position: absolute; bottom: 14px; font-size: 10px; font-weight: 700; color: var(--paper); letter-spacing: .2px; }

  /* About page */
  .about-heading { position: absolute; left: 230px; top: 22px; width: 300px; font-size: 17px; font-weight: 800; color: var(--crimson); }
  .about-copy { position: absolute; left: 230px; top: 48px; width: 190px; font-size: 11.5px; font-weight: 700; color: var(--charcoal); line-height: 1.35; }
  .diagram { position: absolute; left: 430px; top: 22px; width: 112px; height: 120px; border: 2px solid var(--crimson); background: linear-gradient(160deg, #fdf0ef, #f3c9c4); }

  .topic { position: absolute; top: 160px; width: 160px; }
  .topic--watch { left: 18px; }
  .topic--diagnose { left: 200px; }
  .topic--treat { left: 382px; }
  .topic-media { height: 92px; border: 2px solid var(--crimson); }
  .media--xray { background: linear-gradient(135deg, #1b4f8a, #7fb3e0 60%, #e8572f); }
  .media--consult { background: linear-gradient(135deg, #5d7a3a, #c9c1b3 55%, #8b8f7a); }
  .media--monitor { background: linear-gradient(135deg, #f3f3f3, #d9d9d9 50%, #c4141f); }
  .topic-title { margin-top: 8px; font-size: 12px; font-weight: 800; color: var(--crimson); }
  .topic-list { list-style: none; margin-top: 3px; font-size: 10px; font-weight: 700; color: var(--charcoal); line-height: 1.35; }

  /* More page */
  .more-band { position: absolute; left: 0; top: 0; width: 100%; height: 120px; background: var(--crimson); padding: 22px 22px 0 26px; color: var(--paper); }
  .more-heading { font-size: 17px; font-weight: 800; }
  .more-copy { margin-top: 6px; font-size: 10px; font-weight: 700; line-height: 1.35; }
  .symptoms { position: absolute; left: 30px; top: 138px; }
  .symptoms-title { font-size: 12.5px; font-weight: 800; color: var(--crimson); }
  .symptoms-list { margin-top: 6px; list-style: none; font-size: 10.5px; font-weight: 700; color: var(--ink); line-height: 1.35; }
  .symptoms-list li { position: relative; padding-left: 13px; }
  .symptoms-list li::before { content: ""; position: absolute; left: 0; top: 5px; width: 6px; height: 6px; border-radius: 50%; background: var(--crimson); }
  .mesh-heart { position: absolute; right: 46px; top: 150px; width: 150px; height: 170px; border-radius: 40% 40% 50% 50%; background: radial-gradient(circle at 50% 45%, #f4a3aa, #fbe3e5 70%, rgba(255,255,255,0)); }

  /* Cover */
  .cover-strip { position: absolute; left: 0; top: 0; width: 100%; height: 22px; background: var(--maroon); }
  .cover-field { position: absolute; left: 0; top: 22px; width: 100%; height: 368px; background: linear-gradient(90deg, #f2f2f2, #e7e4e2); }
  .cover-frame { position: absolute; left: 0; top: 22px; width: 280px; height: 368px; background: var(--crimson); }
  .cover-heart-image { position: absolute; left: 18px; top: 44px; width: 244px; height: 300px; border-radius: 120px 120px 40px 40px; background: radial-gradient(circle at 45% 45%, #8e2338, #2a0f2f 60%, #120a2a); }
  .cover-portrait { position: absolute; left: 300px; top: 40px; width: 240px; height: 230px; background: linear-gradient(180deg, #ddd7cf, #f1ece6); }
  .brand-box { position: absolute; left: 290px; top: 282px; width: 256px; height: 84px; background: var(--paper); display: flex; align-items: center; gap: 10px; padding: 0 14px; }
  .brand-mark { flex: 0 0 14px; width: 14px; height: 14px; border-radius: 50%; background: var(--crimson); }
  .brand-name { font-size: 15px; font-weight: 700; color: var(--crimson); line-height: 1.2; }
</style>
</head>
<body>

  <!-- Inside left page -->
  <section class="page page--about">
    <h2 class="about-heading">About Arrhythmias:</h2>
    <p class="about-copy">Arrhythmias are disorders of the electrical system of the heart. A common arrhythmia is atrial fibrillation.</p>
    <div class="diagram" role="img" aria-label="Diagram of the heart's electrical conduction pathway"></div>

    <div class="topic topic--watch">
      <div class="topic-media media--xray" role="img" aria-label="Illustration of a glowing heart inside the chest with a heartbeat trace"></div>
      <h3 class="topic-title">What to watch for:</h3>
      <ul class="topic-list">
        <li>Flutters or skipping sensation</li>
        <li>Racing heart beat</li>
        <li>Lightheaded spells or passing out</li>
        <li>Trouble breathing</li>
      </ul>
    </div>
    <div class="topic topic--diagnose">
      <div class="topic-media media--consult" role="img" aria-label="Photo of an older couple outdoors"></div>
      <h3 class="topic-title">How to Diagnose:</h3>
      <ul class="topic-list">
        <li>EKG</li>
        <li>Heart monitor</li>
        <li>EP study</li>
      </ul>
    </div>
    <div class="topic topic--treat">
      <div class="topic-media media--monitor" role="img" aria-label="Photo of a red heart with a stethoscope on an EKG strip"></div>
      <h3 class="topic-title">How to treat:</h3>
      <ul class="topic-list">
        <li>Medications</li>
        <li>Lifestyle change</li>
        <li>Ablation</li>
        <li>Devices</li>
      </ul>
    </div>

    <svg class="footer-band" viewBox="0 0 560 44" preserveAspectRatio="none" aria-hidden="true">
      <polygon points="0,0 560,0 560,44 0,44" fill="var(--charcoal)"/>
      <polygon points="260,0 560,0 560,44 300,44" fill="var(--crimson)"/>
    </svg>
    <span class="footer-url" style="right:24px;">www.harwellheartcare.com</span>
  </section>

  <!-- Inside right page -->
  <section class="page page--more">
    <div class="more-band">
      <h2 class="more-heading">More about Arrhythmia</h2>
      <p class="more-copy">Arrhythmia refers to an abnormality of the electrical system of the heart. This may result in the heart beating too fast or too slow or irregularly. If the heart is not beating correctly, then the heart may not pump as strong as it should. This can cause symptoms.</p>
    </div>
    <div class="symptoms">
      <h3 class="symptoms-title">Symptoms include things such as:</h3>
      <ul class="symptoms-list">
        <li>Skips or flutters in the chest.</li>
        <li>Racing heart beat</li>
        <li>Lightheaded spells</li>
        <li>Passing out spells</li>
        <li>Trouble breathing</li>
      </ul>
    </div>
    <div class="mesh-heart" role="img" aria-label="Low-poly wireframe illustration of a red heart"></div>

    <svg class="footer-band" viewBox="0 0 560 44" preserveAspectRatio="none" aria-hidden="true">
      <polygon points="0,0 250,0 300,44 0,44" fill="var(--crimson)"/>
      <polygon points="250,0 560,0 560,44 300,44" fill="var(--charcoal)"/>
    </svg>
    <span class="footer-url" style="left:24px;">www.harwellheartcare.com</span>
  </section>

  <!-- Front cover -->
  <section class="page page--cover">
    <div class="cover-strip"></div>
    <div class="cover-field"></div>
    <div class="cover-frame"></div>
    <div class="cover-heart-image" role="img" aria-label="Illustration of an anatomical heart over a heartbeat trace"></div>
    <div class="cover-portrait" role="img" aria-label="Photo of a smiling cardiologist in a white coat with a stethoscope"></div>
    <div class="brand-box">
      <span class="brand-mark" aria-hidden="true"></span>
      <span class="brand-name">Harwell Heart and Circulatory Care</span>
    </div>
  </section>

</body>
</html>
```